Mortgage and Asset Finance Broker Needs a Wordpress Website Design

I need a modern looking Wordpress website to showcase my service as a mortgage and asset broker. I have a company and we work with various lenders to arrange mortgages, as well as commercial lending and business asset finance. The website needs to look professional, be easy to navigate and capture leads. SEO is obviously very important to me. It really needs to be something that shows trust and professioanlism.
Updates

On the home page I will need to have some boxes for Home Loans, Refinancing, Business (and Agriculture) Loans etc. I'd like a carousel in the middle which shows our lenders (so that can have the banks logos added).

It needs to be easy top navigate and showcase all we do - Home Loans, Refinancing, Commercial Loans, Car Loans, Asset Finance etc.

There are plenty of companies on the internet that do this.

There is some good information here https://lendquill.example.au/mortgage-broker-homepage/

I need to make sure that editing the website is easy (I think Wordpress has something that allows that).

Also we are very much an Australian business so that is something to advertise.

Industry/Entity Type

Mortgage and Finance Broker

Coding

Coded - Design and coding required

Number of Pages Required

5+ page

Requirements
Must have
• Easy to navigate professional feel. Must be responsive and mobile friendly.
Nice to have
• Homepage with links to inner pages. Contact buttons.

```html
<!DOCTYPE html>
<html lang="en">
<head>
<meta charset="utf-8">
<title>Northvale Finance – Home</title>
<link href="https://fonts.googleapis.com/css2?family=Montserrat:wght@500;600;700;800&family=Inter:wght@400;500;600&family=Lora:wght@500;600&display=swap" rel="stylesheet">
<style>
:root{
  --blue:#1d5faa;
  --blue-deep:#17508f;
  --orange:#f5902b;
  --ink:#1b2330;
  --muted:#5b6676;
  --pale:#eef4fb;
  --line:#d9e3ef;
  --canvas:#f5f6f8;
  --white:#ffffff;
}
*{box-sizing:border-box;margin:0;padding:0}
html,body{width:1200px;height:1200px;overflow:hidden;background:var(--canvas)}
body{font-family:"Inter",sans-serif;color:var(--ink)}
.stage{position:absolute;left:0;top:0;width:1932px;height:1932px;transform:scale(0.62112);transform-origin:0 0}
.page{position:absolute;left:684px;top:0;width:564px;height:1932px;background:var(--white);overflow:hidden}
.sec{position:absolute;left:0;width:564px}
.abs{position:absolute}
.h{font-family:"Montserrat",sans-serif;font-weight:700;text-transform:uppercase;letter-spacing:.1px}
.label{font-family:"Lora",serif;font-weight:600;font-size:5px;color:var(--orange)}
.btn{position:absolute;display:flex;align-items:center;justify-content:center;font-size:4.2px;font-weight:600;color:#fff;background:var(--orange)}
.btn.blue{background:var(--blue)}
.btn.ghost{background:transparent;border:1px solid #fff}
.ph{position:absolute}

.topbar{top:0;height:14px;background:var(--blue);color:#fff;font-size:3.6px}
.topbar .social{left:60px;top:4px;display:flex;gap:7px}
.topbar .social i{width:5px;height:5px;border-radius:50%;background:#fff;opacity:.85;display:block}
.topbar .info{right:60px;top:4.5px;display:flex;gap:8px}
.header{top:14px;height:40px;background:#fff}
.brand{left:57px;top:12px;font-family:"Montserrat",sans-serif;font-weight:800;font-size:12px;color:var(--ink);display:flex;align-items:center;gap:4px}
.brand .dot{width:8px;height:8px;background:var(--blue)}
.nav{left:208px;top:17px;display:flex;gap:18px;font-size:4.6px;font-weight:500}
.nav .on{color:var(--blue)}
.hero{top:54px;height:239px;background:linear-gradient(90deg,#2a2d31 0%,#4b5057 45%,#8a8e93 100%)}
.hero .welcome{left:57px;top:62px;font-family:"Lora",serif;font-weight:600;font-size:6.4px;color:#fff}
.hero h1{left:57px;top:75px;font-size:26px;line-height:27px;color:#fff;font-family:"Montserrat",sans-serif;font-weight:800}
.hero p{left:57px;top:140px;width:240px;font-size:5.8px;line-height:10px;color:#fff}
.about{top:293px;height:212px}
.about h2{left:296px;top:49px;font-size:16px;line-height:18px}
.about p{left:296px;top:92px;width:210px;font-size:4.6px;line-height:8px;color:var(--muted)}
.checks{left:296px;top:129px;width:215px;display:grid;grid-template-columns:1fr 1fr;gap:4px 8px;font-size:4.4px;line-height:7.5px;color:var(--ink)}
.checks span{display:flex;gap:4px}
.checks svg{flex:none;margin-top:1.5px}
.partners{top:505px;height:48px}
.partners .t{left:57px;top:20px;font-family:"Montserrat",sans-serif;font-weight:600;font-size:6px;color:var(--blue)}
.plogo{position:absolute;top:19px;display:flex;align-items:center;gap:3px}
.plogo i{display:block;width:8px;height:8px;border-radius:50%;background:#4a5160}
.plogo b{display:block;width:28px;height:4px;border-radius:2px;background:#8a93a2}
.banner{top:553px;height:163px;background:linear-gradient(90deg,#2c2f33,#5d6066 50%,#3a3d42)}
.banner h2{left:0;width:564px;top:38px;text-align:center;color:#fff;font-size:16px;line-height:17.5px}
.banner p{left:150px;width:264px;top:80px;text-align:center;color:#fff;font-size:4.8px;line-height:8.5px}
.offers{top:716px;height:326px;background:var(--pale)}
.center{left:0;width:564px;text-align:center}
.offers h2{top:47px;font-size:16px;line-height:18px}
.sub{font-size:4.8px;line-height:8.5px;color:var(--ink)}
.card{position:absolute;top:121px;width:146px;height:171px;background:#fff;border-bottom:2px solid var(--blue);box-shadow:0 1px 4px rgba(20,50,90,.12)}
.card .img{left:10px;top:11px;width:125px;height:83px}
.card h3{position:absolute;left:10px;top:101px;font-size:7px;font-family:"Montserrat",sans-serif;font-weight:700}
.card p{position:absolute;left:10px;top:113px;width:125px;font-size:4.6px;line-height:8.2px;color:var(--muted)}
.why{top:1042px;height:203px;background:linear-gradient(120deg,var(--blue-deep),#2370c2 60%,#1a5da6)}
.why h2{left:57px;top:53px;color:#fff;font-size:16px;line-height:17.5px}
.why p{left:57px;top:112px;width:152px;color:#fff;font-size:4.8px;line-height:8.5px}
.feat{position:absolute;top:39px;width:88px;height:107px;background:rgba(255,255,255,.16);padding:12px 10px;color:#fff}
.feat .ic{width:13px;height:13px;border-radius:50%;background:var(--orange);display:flex;align-items:center;justify-content:center}
.feat h4{margin-top:8px;font-size:5.6px;font-weight:600}
.feat p{position:static;margin-top:4px;width:auto;font-size:4.5px;line-height:8.2px;opacity:.75}
.testi{top:1245px;height:258px}
.testi h2{top:46px;font-size:15px}
.tcard{position:absolute;top:104px;width:145px;height:115px;border:2px solid var(--line);padding:12px 12px}
.stars{display:flex;gap:3px;color:var(--orange);font-size:6px}
.tcard p{margin-top:8px;font-size:5px;line-height:9.6px;color:var(--ink)}
.who{position:absolute;left:14px;top:74px;display:flex;align-items:center;gap:8px}
.avatar{width:16px;height:16px;border-radius:50%;background:linear-gradient(#7e8a99,#3d4652)}
.who b{display:block;font-size:4.4px;font-weight:500}
.who small{display:block;font-size:3.8px;color:var(--blue)}
.appt{top:1503px;height:269px;background:linear-gradient(120deg,#1a5aa3,#2472c4)}
.vert{position:absolute;left:24px;top:248px;transform:rotate(-90deg);transform-origin:0 0;font-family:"Montserrat",sans-serif;font-weight:800;font-size:33px;color:rgba(255,255,255,.16);white-space:nowrap}
.appt h2{left:63px;top:45px;color:#fff;font-size:16px;line-height:17.5px}
.appt .lead{left:63px;top:88px;width:210px;color:#fff;font-size:4.6px;line-height:8px}
.pts{left:63px;top:115px;width:210px;color:#fff}
.pts h5{display:flex;gap:4px;align-items:center;font-size:5.4px;font-weight:600;margin-top:6px}
.pts p{font-size:4.6px;line-height:8px;margin-top:2px}
.form{left:295px;top:28px;width:212px;height:212px;background:#fff;padding:17px 17px}
.form h3{font-family:"Montserrat",sans-serif;font-weight:600;font-size:11.5px;color:var(--ink)}
.fgrid{margin-top:8px;display:grid;grid-template-columns:1fr 1fr;gap:7px 10px}
.fld label{display:block;font-size:4.4px;font-weight:500}
.fld div{margin-top:2px;height:12px;border-bottom:1px solid var(--line);font-size:4.2px;color:#8a93a2;padding:3px 5px;display:flex;justify-content:space-between}
.fld.full{grid-column:1/3}
.fld.full div{height:40px}
.form .btn{left:17px;right:17px;top:178px;height:15px;font-size:4.4px}
.footer{top:1772px;height:140px;background:#f7f9fc}
.fbrand{left:57px;top:28px;font-family:"Montserrat",sans-serif;font-weight:800;font-size:22px;color:var(--ink);display:flex;align-items:center;gap:5px}
.fbrand i{display:block;width:14px;height:14px;background:var(--blue)}
.footer .about-t{left:57px;top:84px;width:120px;font-size:4.6px;line-height:8.5px;color:var(--ink)}
.fcol{position:absolute;top:33px;width:82px}
.fcol h6{font-family:"Montserrat",sans-serif;font-size:5px;font-weight:700}
.fcol a{display:block;font-size:4.5px;color:var(--ink);text-decoration:none;padding:3.5px 0;border-bottom:1px solid var(--line);line-height:5px}
.fcol a:first-of-type{margin-top:4px}
.contact{left:372px;top:20px;width:135px;height:99px;border:2px solid var(--line);padding:12px 12px}
.contact h6{font-family:"Montserrat",sans-serif;font-size:5px;font-weight:700}
.contact li{list-style:none;display:flex;gap:4px;font-size:4.5px;line-height:8px;margin-top:2px}
.contact .soc{display:flex;gap:4px;margin-top:6px}
.contact .soc i{display:block;width:11px;height:11px;border-radius:50%;background:var(--orange)}
.bottom{top:1912px;height:20px;background:var(--blue);color:#fff;font-size:3.8px}
</style>
</head>
<body>
<div class="stage">
<main class="page">

  <div class="sec topbar">
    <div class="abs social"><i></i><i></i><i></i><i></i></div>
    <div class="abs info"><span>☏ 123-456-7890</span><span>✉ hello@northvale.example</span><span>◷ Mon – Fri : 09:00-17:00</span></div>
  </div>

  <header class="sec header">
    <div class="abs brand"><span class="dot"></span><span>northvale</span></div>
    <nav class="abs nav"><span class="on">Home</span><span>About Us</span><span>Services</span><span>Testimonials</span><span>FAQs</span><span>Contact Us</span></nav>
    <div class="btn" style="left:459px;top:14px;width:48px;height:13px">Get Started</div>
  </header>

  <section class="sec hero" role="img" aria-label="Photo of a smiling couple meeting with a finance broker at an office table">
    <div class="abs welcome">Welcome To Northvale Finance</div>
    <h1 class="abs">WALK THE PATH<br>TOGETHER</h1>
    <p class="abs">We connect you with the right lenders to secure the best mortgage, commercial loan, or business asset finance tailored to your needs</p>
    <div class="btn blue" style="left:57px;top:172px;width:60px;height:16px">Get Free Quote</div>
    <div class="btn ghost" style="left:124px;top:172px;width:58px;height:16px">Discover More</div>
  </section>

  <section class="sec about">
    <div class="ph" style="left:57px;top:29px;width:211px;height:158px;background:linear-gradient(135deg,#e6e2dc,#b79b7a 55%,#6d7f94)" role="img" aria-label="Photo of a young couple reviewing a tablet on a sofa among moving boxes"></div>
    <div class="abs label" style="left:296px;top:37px">About Us</div>
    <h2 class="abs h">Financing Made Easy,<br>Tailored For You</h2>
    <p class="abs">We are a trusted mortgage and asset brokerage firm, working with a diverse network of lenders to find the perfect financing solution for individuals and businesses.</p>
    <div class="abs checks">
      <span><svg width="5" height="5" viewBox="0 0 10 10"><rect x=".5" y=".5" width="9" height="9" fill="none" stroke="#1d5faa"/><path d="M2 5l2 2 4-4" fill="none" stroke="#1d5faa"/></svg>Access to multiple lenders</span>
      <span><svg width="5" height="5" viewBox="0 0 10 10"><rect x=".5" y=".5" width="9" height="9" fill="none" stroke="#1d5faa"/><path d="M2 5l2 2 4-4" fill="none" stroke="#1d5faa"/></svg>Expert guidance &amp; tailored solutions</span>
      <span><svg width="5" height="5" viewBox="0 0 10 10"><rect x=".5" y=".5" width="9" height="9" fill="none" stroke="#1d5faa"/><path d="M2 5l2 2 4-4" fill="none" stroke="#1d5faa"/></svg>Competitive rates &amp; flexible terms</span>
      <span><svg width="5" height="5" viewBox="0 0 10 10"><rect x=".5" y=".5" width="9" height="9" fill="none" stroke="#1d5faa"/><path d="M2 5l2 2 4-4" fill="none" stroke="#1d5faa"/></svg>Fast &amp; hassle-free application process</span>
    </div>
    <div class="btn blue" style="left:296px;top:165px;width:54px;height:13px">More About Us</div>
  </section>

  <section class="sec partners">
    <div class="abs t">Our Partners :</div>
    <div class="plogo" style="left:136px"><i></i><b></b></div>
    <div class="plogo" style="left:215px"><i></i><b style="width:36px"></b></div>
    <div class="plogo" style="left:296px"><i></i><b style="width:30px"></b></div>
    <div class="plogo" style="left:376px"><i></i><b style="width:32px"></b></div>
    <div class="plogo" style="left:458px"><i style="opacity:.5"></i><b style="width:34px;opacity:.5"></b></div>
  </section>

  <section class="sec banner" role="img" aria-label="Photo of two people shaking hands over a signed agreement">
    <h2 class="abs h">Connecting You To The Right<br>Lender, Every Time</h2>
    <p class="abs">Dapibus consectetur ipsum tortor iaculis pulvinar viverra nec donec. Fringilla consectetur turpis efficitur nisi quisque duis eleifend elementum.</p>
    <div class="btn" style="left:258px;top:110px;width:48px;height:14px">Get In Touch</div>
  </section>

  <section class="sec offers">
    <div class="abs center label" style="top:34px;color:var(--blue)">What We Offer</div>
    <h2 class="abs center h">Navigating Mortgages With<br>Ease And Confidence</h2>
    <p class="abs center sub" style="top:89px">Lorem ipsum dolor sit amet, consectetur adipiscing elit. Ut elit tellus, luctus nec<br>ullamcorper mattis, pulvinar dapibus leo.</p>
    <article class="card" style="left:57px">
      <div class="ph img" style="background:linear-gradient(135deg,#3a3a3a,#a88e72 60%,#d9d2c6)" role="img" aria-label="Photo of a small house model on a desk with pens"></div>
      <h3>MORTGAGE SOLUTIONS</h3>
      <p>Pharetra ultricies sociosqu bibendum lectus ante nunc iaculis. Velit vitae quisque ultrices nullam laoreet fermentum.</p>
      <div class="btn" style="left:10px;top:145px;width:45px;height:14px">Learn More</div>
    </article>
    <article class="card" style="left:209px">
      <div class="ph img" style="background:linear-gradient(135deg,#2b2f36,#7d838c 55%,#d6d8dc)" role="img" aria-label="Photo of hands passing banknotes over paperwork"></div>
      <h3>COMMERCIAL LENDING</h3>
      <p>Pharetra ultricies sociosqu bibendum lectus ante nunc iaculis. Velit vitae quisque ultrices nullam laoreet fermentum.</p>
      <div class="btn" style="left:10px;top:145px;width:45px;height:14px">Learn More</div>
    </article>
    <article class="card" style="left:362px">
      <div class="ph img" style="background:linear-gradient(135deg,#c9a77f,#9fb3c9 55%,#e8edf2)" role="img" aria-label="Photo of colleagues reviewing financial charts"></div>
      <h3>BUSINESS ASSET FINANCE</h3>
      <p>Pharetra ultricies sociosqu bibendum lectus ante nunc iaculis. Velit vitae quisque ultrices nullam laoreet fermentum.</p>
      <div class="btn" style="left:10px;top:145px;width:45px;height:14px">Learn More</div>
    </article>
  </section>

  <section class="sec why">
    <div class="abs label" style="left:57px;top:40px">Why Choose Us</div>
    <h2 class="abs h">Smart Lending.<br>Simple<br>Solutions</h2>
    <p class="abs">Vulputate pretium malesuada posuere suscipit vehicula venenatis eget ex. Mattis sapien ridiculus est nibh lectus suspendisse.</p>
    <div class="btn" style="left:57px;top:150px;width:48px;height:14px">Get In Touch</div>
    <div class="feat" style="left:229px"><div class="ic"><svg width="7" height="7" viewBox="0 0 10 10"><path d="M2 8L8 2M4 2h4v4" fill="none" stroke="#fff" stroke-width="1.3"/></svg></div><h4>Competitivea Pricing</h4><p>Quisque amet sit nascetur fermentum eu erat curabitur aliquet iaculis lacus semper. Dis integer nibh dignissim per nec ut.</p></div>
    <div class="feat" style="left:324px"><div class="ic"><svg width="7" height="7" viewBox="0 0 10 10"><path d="M2 8L8 2M4 2h4v4" fill="none" stroke="#fff" stroke-width="1.3"/></svg></div><h4>Free Consultations</h4><p>Quisque amet sit nascetur fermentum eu erat curabitur aliquet iaculis lacus semper. Dis integer nibh dignissim per nec ut.</p></div>
    <div class="feat" style="left:419px"><div class="ic"><svg width="7" height="7" viewBox="0 0 10 10"><path d="M2 8L8 2M4 2h4v4" fill="none" stroke="#fff" stroke-width="1.3"/></svg></div><h4>Lifetime Tracking</h4><p>Quisque amet sit nascetur fermentum eu erat curabitur aliquet iaculis lacus semper. Dis integer nibh dignissim per nec ut.</p></div>
  </section>

  <section class="sec testi">
    <div class="abs center label" style="top:34px;color:var(--blue)">Testimonials</div>
    <h2 class="abs center h">What Clients Say About Us</h2>
    <p class="abs center sub" style="top:72px">Lorem ipsum dolor sit amet, consectetur adipiscing elit. Ut elit tellus, luctus nec ullamcorper mattis,<br>pulvinar dapibus leo.</p>
    <article class="tcard" style="left:57px"><div class="stars">★ ★ ★ ★ ★</div><p>Porttitor integer bibendum odio pulvinar rutrum magnis viverra orci tincidunt efficitur. Aptent pharetra est nunc mattis donec per mi porttitor.</p><div class="who"><span class="avatar"></span><span><b>Mara T. Ellison</b><small>Customer</small></span></div></article>
    <article class="tcard" style="left:209px"><div class="stars">★ ★ ★ ★ ☆</div><p>Porttitor integer bibendum odio pulvinar rutrum magnis viverra orci tincidunt efficitur. Aptent pharetra est nunc mattis donec per mi porttitor.</p><div class="who"><span class="avatar"></span><span><b>Dean R. Palmer</b><small>Customer</small></span></div></article>
    <article class="tcard" style="left:362px"><div class="stars">★ ★ ★ ★ ★</div><p>Porttitor integer bibendum odio pulvinar rutrum magnis viverra orci tincidunt efficitur. Aptent pharetra est nunc mattis donec per mi porttitor.</p><div class="who"><span class="avatar"></span><span><b>Lena J. Marsh</b><small>Customer</small></span></div></article>
  </section>

  <section class="sec appt">
    <div class="vert">Appointment</div>
    <h2 class="abs h">Let's Talk With A<br>Lending Specialist</h2>
    <p class="abs lead">Vulputate pretium malesuada posuere suscipit vehicula venenatis eget ex. Mattis sapien ridiculus est nibh lectus suspendisse.</p>
    <div class="abs pts">
      <h5>☑ Every Step Of The Way</h5><p>Pharetra tellus aliquet lacus fusce fermentum malesuada sem. Purus suscipit ullamcorper elementum in rhoncus montes.</p>
      <h5>☑ Dedicated Loan Concierge</h5><p>Pharetra tellus aliquet lacus fusce fermentum malesuada sem. Purus suscipit ullamcorper elementum in rhoncus montes.</p>
      <h5>☑ Flexible Rates &amp; Low Fees</h5><p>Pharetra tellus aliquet lacus fusce fermentum malesuada sem. Purus suscipit ullamcorper elementum in rhoncus montes.</p>
    </div>
    <form class="abs form">
      <h3>Make an Appointment</h3>
      <div class="fgrid">
        <div class="fld"><label>First Name</label><div>First Name</div></div>
        <div class="fld"><label>Last Name</label><div>Last Name</div></div>
        <div class="fld"><label>Phone</label><div>Phone</div></div>
        <div class="fld"><label>Email</label><div>Email</div></div>
        <div class="fld"><label>Date</label><div><span>mm/dd/yyyy</span><span>▭</span></div></div>
        <div class="fld"><label>Time</label><div><span>--:-- --</span><span>◷</span></div></div>
        <div class="fld full"><label>Message</label><div>Message</div></div>
      </div>
      <div class="btn">Make Appointment</div>
    </form>
  </section>

  <footer class="sec footer">
    <div class="abs fbrand"><i></i>northvale</div>
    <p class="abs about-t">Nunc senectus justo id ad ultrices dignissim. Volutpat ullamcorper ut arcu tellus metus porttitor phasellus purus.</p>
    <div class="fcol" style="left:192px"><h6>SERVICES</h6><a>Home Loans</a><a>Refinancing</a><a>Commercial Loans</a><a>Car Loans</a><a style="border:0">Asset Finance</a></div>
    <div class="fcol" style="left:282px"><h6>QUICK LINKS</h6><a>Home</a><a>Services</a><a>About Us</a><a>FAQ</a><a style="border:0">Contact Us</a></div>
    <div class="abs contact">
      <h6>GET IN TOUCH</h6>
      <ul style="margin-top:5px">
        <li><span style="color:var(--orange)">⌖</span>Lorem ipsum dolor sit amet, consectetur</li>
        <li><span style="color:var(--orange)">✉</span>hello@northvale.example</li>
        <li><span style="color:var(--orange)">☏</span>123-456-7890</li>
      </ul>
      <div class="soc"><i></i><i></i><i></i><i></i></div>
    </div>
  </footer>

  <div class="sec bottom">
    <span class="abs" style="left:57px;top:7px">Copyright © 2025 | Northvale Finance | All rights reserved.</span>
    <span class="abs" style="right:57px;top:7px">Privacy Policy &nbsp;|&nbsp; Terms &amp; Conditions</span>
  </div>

</main>
</div>
</body>
</html>
```